We are a new company with 2 divisions a medical research and medical product sales. We need a company logo and Business Cards. The design files need to be provided to us in Adobe Photoshop CS 5.1.

Target Market(s)

Medical Community

Industry/Entity Type

Medical

Contact Information for Business Card

Company Name - Harborline Biomedical LLC
Company Address 4150 SW 17th Ave Suite 8, Gainesville Fl 32611

Requirements
Must have
• The design files need to be provided to us in Adobe Photoshop CS 5.1.

```html
<!DOCTYPE html>
<html lang="en">
<head>
<meta charset="utf-8">
<title>Harborline Biomedical LLC – Business Card</title>
<link href="https://fonts.googleapis.com/css2?family=Lato:wght@400;700&display=swap" rel="stylesheet">
<style>
  :root {
    --backdrop: #e9e9ea;
    --card: #ffffff;
    --ink: #2b2b2b;
    --muted: #555555;
    --accent: #d84426;
  }
  html, body {
    margin: 0;
    width: 1200px;
    height: 900px;
    overflow: hidden;
    background: var(--backdrop);
    font-family: "Lato", Arial, sans-serif;
  }
  .business-card {
    position: absolute;
    left: 182px;
    top: 212px;
    width: 836px;
    height: 476px;
    background: var(--card);
    border-radius: 22px;
    overflow: hidden;
    box-shadow: 0 10px 30px rgba(0,0,0,0.12);
  }
  .brand {
    position: absolute;
    left: 72px;
    top: 78px;
  }
  .brand-dot {
    width: 34px;
    height: 34px;
    border-radius: 50%;
    background: var(--accent);
    margin: 0 0 22px 74px;
  }
  .brand-name {
    margin: 0;
    font-weight: 700;
    font-size: 25px;
    line-height: 1.15;
    letter-spacing: 0.5px;
    text-transform: uppercase;
    color: var(--ink);
  }
  .contact {
    position: absolute;
    right: 86px;
    top: 186px;
    text-align: right;
    color: var(--muted);
  }
  .person-name {
    margin: 0;
    font-weight: 700;
    font-size: 25px;
    color: var(--ink);
  }
  .person-title {
    margin: 4px 0 0;
    font-size: 18px;
    color: var(--accent);
  }
  .address {
    margin: 36px 0 0;
    font-style: normal;
    font-size: 19px;
    line-height: 1.3;
  }
  .contact-line {
    display: flex;
    justify-content: flex-end;
    align-items: center;
    gap: 9px;
    font-size: 17px;
    margin-top: 10px;
  }
  .contact-line.phone { margin-top: 16px; font-size: 16px; }
  .contact-line svg { width: 18px; height: 16px; fill: var(--accent); }
  .band {
    position: absolute;
    left: 0;
    bottom: 0;
    width: 836px;
    height: 86px;
  }
  .website {
    position: absolute;
    left: 72px;
    bottom: 44px;
    font-size: 16px;
    color: #ffffff;
  }
</style>
</head>
<body>
  <section class="business-card">
    <div class="brand">
      <div class="brand-dot"></div>
      <p class="brand-name">Harborline<br>Biomedical LLC</p>
    </div>

    <div class="contact">
      <p class="person-name">Name of the Person</p>
      <p class="person-title">Managing Director</p>
      <address class="address">4150 SW 17th Ave Suite 8,<br>Gainesville Fl 32611</address>
      <div class="contact-line phone">
        <span>044 1235 67890</span>
        <svg viewBox="0 0 18 16" aria-hidden="true"><path d="M1 5c0-2 3-4 8-4s8 2 8 4v1h-4V4.5c-1-.5-2.5-.8-4-.8s-3 .3-4 .8V6H1z"/><path d="M4 7l2-2h6l2 2 2 8H2z"/></svg>
      </div>
      <div class="contact-line email">
        <span>info@harborlinebiomedical.com</span>
        <svg viewBox="0 0 18 16" aria-hidden="true"><rect x="0" y="2" width="18" height="13" rx="1"/><path d="M1 3l8 6 8-6" fill="none" stroke="#fff" stroke-width="1.5"/></svg>
      </div>
    </div>

    <svg class="band" viewBox="0 0 836 86" preserveAspectRatio="none" aria-hidden="true">
      <path d="M0 0 H350 C385 0 382 56 430 56 H836 V86 H0 Z" fill="var(--accent)"/>
    </svg>
    <span class="website">www.harborlinebiomedical.com</span>
  </section>
</body>
</html>
```